I have a logo and need to design the business card and stationery.
Updates

The uploaded logo image named as GREYHAVEN CONSTRUCTION which is to be replaced to GREYHAVEN CONTRACTS. Kindly add below details and submit the designs- Company name- Greyhaven Engineering Contracts LLP Name & Post- Kunal Mehra (Designated Partner) Address- Block No.317, Wing C, Tulsi Trade Plaza, Lokhand Marg, Varun Industrial Park, Goregaon(E), Mumbai - 400 063 Contact- +91 97410 58723 Email- kunalmehra@examplemail.com Website- www.greyhavencontracts.example Contact for Letterhead- +91-22-28145597

Hi Tanvir Rahman, We are liking your Design #41927506. We have suggested some changes which are mentioned in feedback. Kindly revert with it asap to finalize this design.

Colors

Designer to choose colors to be used in the design.

```html
<!DOCTYPE html>
<html lang="en">
<head>
<meta charset="utf-8">
<title>Greyhaven Construction — Stationery Set</title>
<link rel="stylesheet" href="https://fonts.googleapis.com/css2?family=Source+Sans+3:wght@300;400;600&display=swap">
<style>
:root{
  --backdrop:#96979b;
  --paper:#ffffff;
  --ink:#333335;
  --ink-soft:#555558;
  --band:#232323;
  --rule:#4a90c8;
  --window:#d4d5d7;
  --folder:#5b5b5d;
  --folder-flap:#656567;
}
*{box-sizing:border-box;margin:0;padding:0}
html,body{width:1000px;height:1200px;overflow:hidden}
body{background:var(--backdrop);font-family:"Source Sans 3",sans-serif;color:var(--ink);position:relative}
.piece{position:absolute;background:var(--paper);overflow:hidden}

/* brand lockup */
.brand{position:absolute;display:flex;flex-direction:column;align-items:center;font-weight:600;color:var(--ink);text-align:center;line-height:1}
.brand .mark{width:var(--m);height:var(--m);background:var(--ink);margin-bottom:calc(var(--m)*0.18)}
.brand .name{font-size:var(--f);letter-spacing:.04em}
.brand .sub{font-size:calc(var(--f)*0.62);letter-spacing:.32em;margin-top:2px}

.contact{position:absolute;font-size:10px;color:var(--ink-soft);line-height:1}
.contact li{list-style:none;display:flex;align-items:center;gap:5px;white-space:nowrap}
.contact svg{width:9px;height:9px;fill:var(--ink-soft);flex:none}
.title-text{position:absolute;font-weight:400;color:var(--ink-soft);letter-spacing:.01em}
.band{position:absolute;left:0;right:0;bottom:0;background:var(--band)}

/* letterhead */
.letterhead .rule{position:absolute;left:0;right:0;top:82px;height:1px;background:var(--rule)}
.letter-body{position:absolute;left:50px;top:118px;width:274px;font-size:8.1px;line-height:10.2px;text-align:justify;color:var(--ink)}
.letter-body p{margin-bottom:10px}

/* notebook */
.notebook{background:linear-gradient(135deg,#fbfbf9,#e6e6e1)}
.notebook .edge{position:absolute;left:0;right:0;height:7px;background:var(--band)}
.spiral{position:absolute;left:822px;top:565px;width:18px;height:195px}
.spiral i{display:block;height:3px;width:16px;margin-bottom:12.2px;border-radius:2px;background:#fff;border:1px solid #444}

/* folder */
.folder{background:var(--folder)}
.folder .flap{position:absolute;left:0;right:0;top:0;height:20px;background:var(--folder-flap);border-radius:0 0 8px 8px}
.folder .button{position:absolute;left:64px;top:15px;width:11px;height:11px;border-radius:50%;background:#1e1e1e}
.mini-card{position:absolute;left:45px;top:119px;width:52px;height:74px;background:var(--paper)}
.mini-card ul{position:absolute;left:8px;top:47px;font-size:2.4px;line-height:3.2px;color:var(--ink-soft);list-style:none}
</style>
</head>
<body>

<!-- business card front -->
<section class="piece card-front" style="left:38px;top:51px;width:356px;height:199px">
  <div class="brand" style="left:0;right:0;top:57px;--m:42px;--f:14px">
    <span class="mark"></span><span class="name">GREYHAVEN</span><span class="sub">CONSTRUCTION</span>
  </div>
  <ul class="contact" style="left:65px;top:170px;font-size:4px">
    <li><svg viewBox="0 0 10 10"><path d="M5 0a3.5 3.5 0 0 0-3.5 3.5C1.5 6 5 10 5 10s3.5-4 3.5-6.5A3.5 3.5 0 0 0 5 0z"/></svg>Block No.317, Wing C, Tulsi Trade Plaza, Lokhand Marg</li>
  </ul>
  <ul class="contact" style="left:191px;top:172px;font-size:10px">
    <li><svg viewBox="0 0 10 10"><circle cx="5" cy="5" r="5"/></svg>www.greyhavencontracts.example</li>
  </ul>
</section>

<!-- envelope front -->
<section class="piece envelope" style="left:444px;top:47px;width:526px;height:207px">
  <div class="brand" style="left:38px;width:138px;top:16px;--m:42px;--f:14px">
    <span class="mark"></span><span class="name">GREYHAVEN</span><span class="sub">CONSTRUCTION</span>
  </div>
  <ul class="contact" style="left:18px;top:97px;font-size:9.5px">
    <li style="margin-bottom:6px"><svg viewBox="0 0 10 10"><path d="M5 0 0 4v6h10V4z"/></svg>Block No.317, Wing C, Tulsi Trade Plaza, Lokhand Marg</li>
    <li style="font-size:7.5px;margin-bottom:5px"><svg viewBox="0 0 10 10"><path d="M2 0h2l1 3-1.5 1a6 6 0 0 0 2.5 2.5L7 5l3 1v2c0 1-1 2-2 2C4 10 0 6 0 2 0 1 1 0 2 0z"/></svg>Contact- +91 97410 58723</li>
    <li style="margin-bottom:6px"><svg viewBox="0 0 10 10"><path d="M0 2h10v6H0zM1 3l4 3 4-3" fill="none" stroke="#555" stroke-width="1"/></svg>Email- kunalmehra@examplemail.com</li>
    <li><svg viewBox="0 0 10 10"><circle cx="5" cy="5" r="5" fill="#999"/></svg>www.greyhavencontracts.example</li>
  </ul>
  <div style="position:absolute;left:301px;top:65px;width:163px;height:69px;border-radius:8px;background:var(--window)"></div>
  <div class="band" style="height:26px"></div>
</section>

<!-- business card back -->
<section class="piece card-back" style="left:76px;top:319px;width:356px;height:200px">
  <div class="brand" style="left:0;width:138px;top:46px;--m:42px;--f:14px">
    <span class="mark"></span><span class="name">GREYHAVEN</span><span class="sub">CONSTRUCTION</span>
  </div>
  <div style="position:absolute;left:139px;top:42px;width:1px;height:100px;background:#555"></div>
  <div class="title-text" style="left:149px;top:40px;font-size:11px">GREYHAVEN CONSTRUCTION</div>
  <ul class="contact" style="left:154px;top:102px">
    <li style="font-size:7.5px;margin-bottom:8px"><svg viewBox="0 0 10 10"><path d="M2 0h2l1 3-1.5 1a6 6 0 0 0 2.5 2.5L7 5l3 1v2c0 1-1 2-2 2C4 10 0 6 0 2 0 1 1 0 2 0z"/></svg>Contact- +91 97410 58723</li>
    <li style="margin-bottom:6px"><svg viewBox="0 0 10 10"><path d="M0 2h10v6H0zM1 3l4 3 4-3" fill="none" stroke="#555" stroke-width="1"/></svg>Email- kunalmehra@examplemail.com</li>
    <li><svg viewBox="0 0 10 10"><circle cx="5" cy="5" r="5"/></svg>www.greyhavencontracts.example</li>
  </ul>
</section>

<!-- envelope back -->
<section class="piece envelope-back" style="left:447px;top:293px;width:527px;height:206px">
  <svg style="position:absolute;left:0;top:0" width="527" height="64" viewBox="0 0 527 64"><polygon points="-4,0 527,0 490,64 27,64" fill="var(--band)"/></svg>
  <div class="brand" style="left:0;right:0;top:90px;--m:42px;--f:14px">
    <span class="mark"></span><span class="name">GREYHAVEN</span><span class="sub">CONSTRUCTION</span>
  </div>
</section>

<!-- letterhead with letter -->
<section class="piece letterhead" style="left:29px;top:562px;width:375px;height:500px">
  <div class="brand" style="left:58px;width:140px;top:5px;--m:42px;--f:14px">
    <span class="mark"></span><span class="name">GREYHAVEN</span><span class="sub">CONSTRUCTION</span>
  </div>
  <div class="title-text" style="left:212px;top:45px;font-size:11px">GREYHAVEN CONSTRUCTION</div>
  <div class="rule"></div>
  <div class="letter-body">
    <p style="margin-left:4px">orem ipsum dolor sit amet,</p>
    <p style="margin-top:4px">scelerisque. Nam sapien odio, posuere ut ornare eget, sodales eget nibh. Nunc sed nunc lectus. Donec pharetra lobortis nulla, sit amet laoreet mauris ultricies at. Nulla tristique dui hendrerit urna rhoncus pellentesque. Cras vestibulum consectetur arcu, nec faucibus odio auctor at. Curabitur id congue ex. In lobortis vel risus quis porttitor. Vestibulum pellentesque quis tellus sed congue. Curabitur tristique posuere massa, id ultrices nulla tempus tincidunt. Vivamus sit amet enim sem. Quisque porta interdum arcu, sed dapibus magna. Praesent facilisis enim ac ante gravida rutrum.</p>
    <p>Phasellus vel lectus aliquam dui elementum lacinia. Donec et orci iaculis, rutrum augue eget, elementum leo. Curabitur congue libero id mi pulvinar porta. Ut varius enim cursus, lobortis leo sed, facilisis mi. Vivamus pellentesque id ipsum pharetra condimentum. Ut vitae commodo tellus. In eget eros sit amet velit tincidunt ornare. Sed mollis dolor eu condimentum mollis. Mauris vel blandit arcu. Aenean nec placerat lectus. Curabitur placerat id tortor nec consectetur. Nunc sed elit purus. Ut tellus eros, ullamcorper tristique odio quis, elementum molestie urna. Class aptent taciti sociosqu ad litora torquent per conubia nostra, per inceptos himenaeos.</p>
    <p>Maecenas iaculis vulputate dignissim. Nullam lorem felis, mattis vel libero a, imperdiet facilisis orci. Nullam facilisis mi eu arcu ultricies, ac sagittis sem tempus. Proin ullamcorper neque eu mi dapibus, vitae consequat lacus aliquet. Proin posuere ex nec tempus faucibus. Aenean scelerisque nisi justo, sit amet cursus leo euismod ut. Morbi maximus, sapien quis tincidunt ornare, quam nibh hendrerit mauris, id ultricies lorem orci vel dui. Phasellus consectetur sapien a risus convallis dapibus. Sed a tempor libero. Nam quis libero ligula. Morbi eget velit eu sapien finibus iaculis nec tincidunt orci. Donec sodales erat laoreet nisl interdum volutpat.</p>
    <p style="margin-top:28px">Morbi eget velit eu</p>
  </div>
  <div class="band" style="height:18px"></div>
</section>

<!-- blank letterhead -->
<section class="piece letterhead" style="left:442px;top:562px;width:375px;height:500px">
  <div class="brand" style="left:40px;width:140px;top:4px;--m:42px;--f:14px">
    <span class="mark"></span><span class="name">GREYHAVEN</span><span class="sub">CONSTRUCTION</span>
  </div>
  <div class="title-text" style="left:210px;top:49px;font-size:11px">GREYHAVEN CONSTRUCTION</div>
  <div class="rule"></div>
  <div class="band" style="height:18px"></div>
</section>

<!-- notebook -->
<section class="piece notebook" style="left:830px;top:563px;width:140px;height:197px">
  <div class="edge" style="top:0"></div>
  <div class="edge" style="bottom:0"></div>
  <div class="brand" style="left:0;right:0;top:80px;--m:26px;--f:9px">
    <span class="mark"></span><span class="name">GREYHAVEN</span><span class="sub">CONSTRUCTION</span>
  </div>
</section>
<div class="spiral"><i></i><i></i><i></i><i></i><i></i><i></i><i></i><i></i><i></i><i></i><i></i><i></i><i></i></div>

<!-- presentation folder -->
<section class="piece folder" style="left:835px;top:807px;width:138px;height:197px">
  <div class="flap"></div>
  <div class="button"></div>
  <div class="mini-card">
    <div class="brand" style="left:0;right:0;top:12px;--m:13px;--f:4.5px">
      <span class="mark"></span><span class="name">GREYHAVEN</span><span class="sub">CONSTRUCTION</span>
    </div>
    <ul>
      <li>Block 317, Tulsi Plaza</li>
      <li>Goregaon East 400063</li>
      <li>+91 97410 58723</li>
      <li>info@greyhaven.example</li>
      <li>www.greyhaven.example</li>
    </ul>
  </div>
</section>

</body>
</html>
```